Pet store web design

I would like to redesign my current online store (http://brindlecorner.com)
I'm looking for a clean, modern design. Any ideas are welcome..

Industry/Entity Type

Pet

Number of Pages Required

3 page

```html
<!DOCTYPE html>
<html lang="en">
<head>
<meta charset="utf-8">
<title>Brindle Corner – Pet Store</title>
<link rel="stylesheet" href="https://fonts.googleapis.com/css2?family=Open+Sans:wght@400;600;700&family=Fredoka:wght@500;600&display=swap">
<style>
:root{
  --teal:#2fa3a0;
  --teal-dark:#23807e;
  --orange:#f26b21;
  --red:#e2412d;
  --ink:#3b3f45;
  --muted:#8a8f96;
  --line:#e1e3e6;
  --page:#f1f2f3;
  --white:#ffffff;
  --footer:#59636d;
  --footer-dark:#48515a;
  --hero-a:#6e8aa0;
  --hero-b:#a7b9a2;
}
*{box-sizing:border-box;margin:0;padding:0}
html,body{width:1200px;height:2464px;overflow:hidden}
body{position:relative;background:var(--page);font-family:"Open Sans",Arial,sans-serif;color:var(--ink);font-size:14px}
.abs{position:absolute}
.display{font-family:"Fredoka","Open Sans",sans-serif}

/* top bar */
.topbar{left:0;top:0;width:1200px;height:44px;background:var(--teal)}
.topbar-links{position:absolute;left:580px;top:0;height:44px;display:flex;gap:34px;align-items:center;color:var(--white);font-size:13px;font-weight:600}
.topbar-links span::before{content:"";display:inline-block;width:9px;height:9px;border-radius:50%;background:var(--white);margin-right:7px;vertical-align:middle;opacity:.85}

/* header */
.header{left:0;top:44px;width:1200px;height:106px;background:var(--white)}
.brand{position:absolute;left:110px;top:30px;display:flex;align-items:center;gap:12px}
.brand-mark{width:40px;height:40px;border-radius:50%;background:var(--orange)}
.brand-name{font-family:"Fredoka",sans-serif;font-weight:600;font-size:34px;color:var(--orange)}
.search{position:absolute;left:700px;top:20px;width:230px;height:32px;border:1px solid var(--line);border-radius:3px;display:flex}
.search-field{flex:1;padding:6px 10px;color:var(--muted);font-size:12px}
.search-btn{width:34px;background:var(--orange);display:flex;align-items:center;justify-content:center}
.cart{position:absolute;left:1010px;top:6px;width:120px;height:72px;background:var(--orange);border-radius:4px;color:var(--white);padding:10px 12px;font-size:12px;font-weight:700;line-height:1.4}
.cart b{display:block;font-size:20px}

/* hero */
.hero{left:0;top:150px;width:1200px;height:430px;background:linear-gradient(110deg,var(--hero-a),var(--hero-b) 60%,#d9c9a8)}
.nav{position:absolute;left:140px;top:14px;display:flex;gap:22px}
.nav-tab{padding:9px 18px;background:var(--white);color:var(--ink);font-weight:600;font-size:14px;border-radius:3px;box-shadow:0 2px 4px rgba(0,0,0,.2);transform:rotate(-3deg)}
.nav-tab:nth-child(even){transform:rotate(3deg)}
.nav-tab.active{background:var(--orange);color:var(--white)}
.hero-title{position:absolute;left:120px;top:278px;font-size:50px;color:var(--white);font-weight:600;text-shadow:0 2px 6px rgba(0,0,0,.3)}
.btn{display:inline-block;background:var(--orange);color:var(--white);font-weight:700;border-radius:3px}
.hero-btn{position:absolute;left:120px;top:362px;padding:12px 26px;font-size:16px}
.hero-dots{position:absolute;left:128px;top:445px;display:flex;gap:8px}
.hero-dots i{width:12px;height:12px;border-radius:50%;background:#c9ccd0}
.hero-dots i:first-child{background:var(--red)}

/* welcome */
.welcome{left:110px;top:630px;width:590px;height:240px;background:var(--white);border:1px solid var(--line);padding:22px 26px}
.welcome-title{display:inline-block;background:var(--orange);color:var(--white);font-size:22px;padding:4px 18px;border-radius:3px;margin-bottom:16px}
.welcome p{font-size:12px;line-height:1.65;color:var(--muted)}
.welcome .btn{margin-top:14px;padding:6px 16px;font-size:12px;background:#f6b31b;color:var(--ink)}
.video{left:730px;top:630px;width:360px;height:240px}
.video-title{font-size:24px;color:var(--teal);margin-bottom:8px}
.video-frame{width:360px;height:200px;background:linear-gradient(135deg,#b69a7a,#e6ddd0);border:6px solid var(--white);box-shadow:0 1px 3px rgba(0,0,0,.2);position:relative}
.video-play{position:absolute;left:150px;top:65px;width:52px;height:52px;border-radius:50%;background:rgba(0,0,0,.45)}
.video-play::after{content:"";position:absolute;left:20px;top:15px;border-left:18px solid var(--white);border-top:11px solid transparent;border-bottom:11px solid transparent}

/* promos */
.promo{left:110px;width:270px;color:var(--white);text-align:center}
.promo-clear{top:920px;height:230px;background:var(--red);padding:22px 18px;text-align:left}
.promo-clear .big{font-size:30px;line-height:1.1}
.promo-clear .pct{font-size:52px;line-height:1}
.promo-clear .sub{font-size:16px;margin-top:10px;color:#ffd9cf}
.promo-clear .shop{position:absolute;right:18px;bottom:18px;font-weight:700;font-size:18px}
.promo-clear .tag{position:absolute;right:20px;top:18px;width:54px;height:54px;border-radius:50%;background:var(--orange)}
.promo-ship{top:1166px;height:150px;background:var(--teal);padding:24px}
.promo-ship .big{font-size:34px;line-height:1.1}
.promo-ship .sub{font-size:18px;margin-top:6px}
.promo-pet{top:1334px;height:186px;background:var(--red);padding:18px}
.promo-pet .art{height:70px;background:linear-gradient(90deg,#f3a48f,#f7d0c2);margin-bottom:10px}
.promo-pet .big{font-size:20px}
.promo-pet .btn{background:var(--white);color:var(--red);padding:5px 18px;font-size:13px;margin-top:8px}
.promo-pet .sub{font-size:11px;margin-top:8px;font-weight:700}

/* popular */
.popular{left:400px;top:920px;width:690px}
.section-bar{height:40px;background:var(--footer);color:var(--white);font-size:18px;padding:8px 18px;margin-bottom:16px}
.grid{display:grid;grid-template-columns:repeat(3,218px);gap:16px 18px}
.card{background:var(--white);border:1px solid var(--line);height:256px;padding:12px;text-align:center;position:relative}
.card-img{height:120px;background:linear-gradient(180deg,#c99a6b,#efe4d6)}
.card-img.cage{background:linear-gradient(180deg,#b9bdc2,#eef0f2)}
.card-img.bed{background:radial-gradient(circle,#3a3d42 35%,#f3f3f3 40%)}
.badge{position:absolute;right:8px;top:8px;background:var(--teal);color:var(--white);font-size:10px;font-weight:700;padding:3px 6px;border-radius:3px}
.price{font-size:20px;font-weight:600;margin-top:10px}
.desc{font-size:11px;color:var(--muted);line-height:1.4;margin-top:4px}
.card-actions{display:flex;justify-content:center;gap:8px;margin-top:10px}
.card-actions .btn{font-size:11px;padding:5px 12px;background:var(--red)}
.fav{width:26px;height:24px;border:1px solid var(--line);border-radius:3px;display:flex;align-items:center;justify-content:center}
.deco{background:#5f6670;opacity:.7}

/* newsletter */
.newsletter{left:0;top:1540px;width:1200px;height:260px;background:var(--white)}
.news-plane{position:absolute;left:230px;top:70px}
.news-text{position:absolute;left:330px;top:40px;width:470px;text-align:center}
.news-text h3{font-size:19px;font-weight:700;line-height:1.4}
.news-text p{font-size:12px;color:var(--muted);margin-top:10px;line-height:1.5}
.news-form{display:flex;justify-content:center;margin-top:18px}
.news-input{width:270px;height:38px;border:1px solid var(--line);border-radius:20px 0 0 20px;padding:10px 16px;font-size:12px;color:var(--muted);text-align:left}
.news-submit{background:var(--orange);color:var(--white);font-weight:700;padding:10px 22px;border-radius:0 20px 20px 0;font-size:13px}
.news-photo{position:absolute;left:830px;top:10px;width:270px;height:250px;background:radial-gradient(ellipse at 50% 60%,#d8a36a,#f3e3c8 70%,var(--white));border-radius:50% 50% 0 0}

/* features */
.features{left:110px;top:1830px;width:980px;display:grid;grid-template-columns:repeat(4,1fr);gap:24px}
.feature{background:var(--white);border-radius:8px;height:100px;display:flex;align-items:center;gap:14px;padding:0 18px;border:2px solid var(--line)}
.feature:nth-child(1){border-color:#f6b31b}
.feature:nth-child(2){border-color:var(--footer)}
.feature:nth-child(3){border-color:var(--red)}
.feature:nth-child(4){border-color:var(--teal)}
.feature-ic{width:54px;height:54px;border-radius:50%;display:flex;align-items:center;justify-content:center;flex:none}
.feature h4{font-size:16px;font-weight:700}
.feature span{font-size:10px;color:var(--muted);letter-spacing:.5px;text-transform:uppercase}

/* footer */
.footer{left:0;top:2010px;width:1200px;height:380px;background:var(--footer);color:#e6e9ec}
.foot-col{position:absolute;top:40px}
.foot-col h5{font-size:15px;font-weight:700;color:var(--white);margin-bottom:14px}
.foot-col li{list-style:none;font-size:12px;line-height:2.1}
.foot-col li::before{content:"›";margin-right:8px;color:#aeb5bc}
.foot-brand{position:absolute;left:930px;top:90px;font-family:"Fredoka",sans-serif;font-weight:600;font-size:26px;color:var(--white)}
.socials{position:absolute;left:930px;top:140px;display:flex;gap:10px}
.socials i{width:34px;height:34px;border-radius:50%;background:var(--footer-dark);border:1px solid #7b858f}
.bottom{left:0;top:2390px;width:1200px;height:74px;background:var(--white);display:flex;align-items:center;justify-content:space-between;padding:0 110px;font-size:11px;color:var(--muted)}
.pay{display:flex;gap:8px;align-items:center}
.pay i{width:40px;height:26px;border-radius:3px;background:#d3d7db}
.pay i:nth-child(2){background:#c8ced4}
</style>
</head>
<body>

<div class="abs topbar">
  <div class="topbar-links"><span>Login</span><span>My Account</span><span>My Wishlist</span><span>Check Out</span></div>
</div>

<header class="abs header">
  <div class="brand"><div class="brand-mark"></div><div class="brand-name">Brindle Corner</div></div>
  <div class="search"><div class="search-field">Search</div><div class="search-btn">
    <svg width="16" height="16" viewBox="0 0 16 16"><circle cx="7" cy="7" r="5" fill="none" stroke="#fff" stroke-width="2"/><line x1="11" y1="11" x2="15" y2="15" stroke="#fff" stroke-width="2"/></svg>
  </div></div>
  <div class="cart">Cart<b>$0.00</b>0 items</div>
</header>

<section class="abs hero" role="img" aria-label="Photo of a happy dog on a bridge">
  <nav class="nav">
    <span class="nav-tab active">Home</span><span class="nav-tab">Dogs</span><span class="nav-tab">Cats</span><span class="nav-tab">Fish</span><span class="nav-tab">Birds</span><span class="nav-tab">Small Pet</span><span class="nav-tab">Contact Us</span>
  </nav>
  <h1 class="hero-title">Brindle Corner</h1>
  <span class="btn hero-btn">Shop The Collection</span>
  <div class="hero-dots"><i></i><i></i><i></i><i></i></div>
</section>

<section class="abs welcome">
  <h2 class="welcome-title display">Welcome to Brindle Corner</h2>
  <p>Welcome to our little corner for pets and the people who love them. We stock food, toys, beds, cages and care products for dogs, cats, birds, fish and small pets, all picked by our own team. Every order is packed with care and shipped quickly to your door. Browse our latest arrivals, find a great deal in our clearance range, and give your companion something new to enjoy today.</p>
  <span class="btn">Read More</span>
</section>

<section class="abs video">
  <h2 class="video-title display">Watch Video</h2>
  <div class="video-frame" role="img" aria-label="Video still of a puppy with a soft toy"><div class="video-play"></div></div>
</section>

<aside class="abs promo promo-clear">
  <div class="tag"></div>
  <div class="big display">CLEARANCE</div>
  <div>Save up to</div>
  <div class="pct display">90%</div>
  <div class="sub display">Pet Gates Extentions</div>
  <div class="shop">SHOP NOW</div>
</aside>
<aside class="abs promo promo-ship">
  <div class="big display">FREE<br>SHIPPING</div>
  <div class="sub">Orders Over $75</div>
</aside>
<aside class="abs promo promo-pet">
  <div class="art" role="img" aria-label="Illustration of small pets"></div>
  <div class="big display">SMALL PET PRODUCTS</div>
  <span class="btn">Buy Now</span>
  <div class="sub">LIMITED QUANTITIES</div>
</aside>

<section class="abs popular">
  <div class="section-bar display">MOST POPULAR</div>
  <div class="grid">
    <article class="card"><span class="badge">Sale</span><div class="card-img" role="img" aria-label="Wooden rabbit hutch"></div><div class="price">$65.93</div><div class="desc">Two storey wooden hutch with run and ramp</div><div class="card-actions"><span class="btn">Add To Cart</span><span class="fav"><svg width="12" height="11" viewBox="0 0 12 11"><path d="M6 10 1 5a2.6 2.6 0 0 1 5-3 2.6 2.6 0 0 1 5 3z" fill="#e2412d"/></svg></span></div></article>
    <article class="card"><div class="card-img cage" role="img" aria-label="Metal pet cage on stand"></div><div class="price">$86.00</div><div class="desc">Large metal cage on wheels with tray</div><div class="card-actions"><span class="btn">Add To Cart</span><span class="fav"><svg width="12" height="11" viewBox="0 0 12 11"><path d="M6 10 1 5a2.6 2.6 0 0 1 5-3 2.6 2.6 0 0 1 5 3z" fill="#e2412d"/></svg></span></div></article>
    <article class="card"><div class="card-img bed" role="img" aria-label="Round raised pet bed"></div><div class="price">$45.20</div><div class="desc">Round raised bed with soft padded cover</div><div class="card-actions"><span class="btn">Add To Cart</span><span class="fav"><svg width="12" height="11" viewBox="0 0 12 11"><path d="M6 10 1 5a2.6 2.6 0 0 1 5-3 2.6 2.6 0 0 1 5 3z" fill="#e2412d"/></svg></span></div></article>
    <article class="card"><span class="badge">Sale</span><div class="card-img" role="img" aria-label="Wooden rabbit hutch"></div><div class="price">$65.93</div><div class="desc">Two storey wooden hutch with run and ramp</div><div class="card-actions"><span class="btn">Add To Cart</span><span class="fav"><svg width="12" height="11" viewBox="0 0 12 11"><path d="M6 10 1 5a2.6 2.6 0 0 1 5-3 2.6 2.6 0 0 1 5 3z" fill="#e2412d"/></svg></span></div></article>
    <article class="card"><div class="card-img cage" role="img" aria-label="Metal pet cage on stand"></div><div class="price">$86.00</div><div class="desc">Large metal cage on wheels with tray</div><div class="card-actions"><span class="btn">Add To Cart</span><span class="fav"><svg width="12" height="11" viewBox="0 0 12 11"><path d="M6 10 1 5a2.6 2.6 0 0 1 5-3 2.6 2.6 0 0 1 5 3z" fill="#e2412d"/></svg></span></div></article>
    <article class="card"><div class="card-img bed" role="img" aria-label="Round raised pet bed"></div><div class="price">$45.20</div><div class="desc">Round raised bed with soft padded cover</div><div class="card-actions"><span class="btn">Add To Cart</span><span class="fav"><svg width="12" height="11" viewBox="0 0 12 11"><path d="M6 10 1 5a2.6 2.6 0 0 1 5-3 2.6 2.6 0 0 1 5 3z" fill="#e2412d"/></svg></span></div></article>
  </div>
</section>

<div class="abs deco" style="left:40px;top:1480px;width:50px;height:70px" role="img" aria-label="Cat silhouette"></div>
<div class="abs deco" style="left:1110px;top:1490px;width:60px;height:60px" role="img" aria-label="Cat silhouette"></div>

<section class="abs newsletter">
  <svg class="news-plane" width="70" height="50" viewBox="0 0 70 50"><path d="M2 22 68 2 40 48 32 30z" fill="none" stroke="#8a8f96" stroke-width="2"/><path d="M32 30 68 2" stroke="#8a8f96" stroke-width="2"/></svg>
  <div class="news-text">
    <h3>Keep Up To Date On The Latest From Brindlecorner.<br>We Love Pets.</h3>
    <p>Get the latest deals and news from our store.<br>Sign up below to hear about offers first.</p>
    <div class="news-form"><div class="news-input">Your Email Address</div><div class="news-submit">SUBMIT</div></div>
  </div>
  <div class="news-photo" role="img" aria-label="Photo of a woman hugging her dog"></div>
</section>

<section class="abs features">
  <div class="feature"><div class="feature-ic" style="background:#f6b31b"><svg width="28" height="20" viewBox="0 0 28 20"><rect x="1" y="3" width="16" height="11" fill="#fff"/><path d="M17 7h6l4 4v3H17z" fill="#fff"/><circle cx="7" cy="16" r="3" fill="#fff"/><circle cx="22" cy="16" r="3" fill="#fff"/></svg></div><div><h4>Delivery</h4><span>Information</span></div></div>
  <div class="feature"><div class="feature-ic" style="background:var(--footer)"><svg width="24" height="24" viewBox="0 0 24 24"><path d="M4 12a8 8 0 1 0 3-6" fill="none" stroke="#fff" stroke-width="2.5"/><path d="M3 2v6h6" fill="none" stroke="#fff" stroke-width="2.5"/></svg></div><div><h4>Returns</h4><span>Query?</span></div></div>
  <div class="feature"><div class="feature-ic" style="background:var(--red)"><svg width="26" height="22" viewBox="0 0 26 22"><path d="M2 2h22v14H10l-6 5v-5H2z" fill="#fff"/></svg></div><div><h4>Questions?</h4><span>View FAQs</span></div></div>
  <div class="feature"><div class="feature-ic" style="background:var(--teal)"><svg width="22" height="22" viewBox="0 0 22 22"><path d="M5 2l4 4-2 3c1 3 3 5 6 6l3-2 4 4-3 3C9 20 2 13 2 5z" fill="#fff"/></svg></div><div><h4>Let Us Help</h4><span>Contact Us</span></div></div>
</section>

<footer class="abs footer">
  <div class="foot-col" style="left:110px"><h5>Shop Now</h5><ul><li>Dogs</li><li>Cats</li><li>Fish</li><li>Birds</li><li>Pet Gates</li><li>Small Animal</li></ul></div>
  <div class="foot-col" style="left:360px"><h5>Shopping Online</h5><ul><li>Delivery Information</li><li>Privacy Policy</li><li>Returns Policy</li><li>Terms and Conditions</li><li>FAQs</li></ul></div>
  <div class="foot-col" style="left:640px"><h5>About Us</h5><ul><li>About Us</li><li>Contact</li><li>Our Blog</li><li>Careers</li></ul></div>
  <div class="foot-brand">BrindleCorner</div>
  <div class="socials"><i></i><i></i><i></i><i></i></div>
</footer>

<div class="abs bottom">
  <span>© 2016 Brindlecorner. All Rights Reserved.</span>
  <div class="pay"><span>Shop in Safety</span><i></i><i></i><i></i><i></i></div>
</div>

</body>
</html>
```